Carpentry Fitouts business Van half wrap

We are looking for a half wrap on our 2020Mitsubishi Express van.
Template attached, base colour to be white

Van colour is white. The 2 blue colours from logo plus black should be used in the half wrap

Our services are :
Commercial Carpentry
Interior Fitouts
Plastering
Suspended Ceilings
Windows & Doors

Rear window to have perforated one way film

Contact details on van should be PH:0412 905 638
dale@keelstonebuilds.com.au

Industry/Entity Type

Carpentry Fitouts

Colors
0054AA
0677BA
7BADD7
CADEEF
E8F1F8
0094D4
00A9DD
6FCCEA
C7EBF8
E9F6FB

Requirements
Nice to have
• Wrap not through door handles

```html
<!DOCTYPE html>
<html lang="en">
<head>
<meta charset="utf-8">
<title>Keelstone Builds – Van Half Wrap</title>
<link rel="stylesheet" href="https://fonts.googleapis.com/css2?family=Antonio:wght@300&family=Oswald:wght@500&family=Roboto+Condensed:wght@400&display=swap">
<style>
  :root {
    --navy: #1f2a66;
    --cyan: #2aa9d6;
    --white: #ffffff;
    --ink: #161616;
    --backdrop: #e6e7e9;
  }
  html, body {
    margin: 0;
    padding: 0;
    width: 1200px;
    height: 667px;
    overflow: hidden;
    background: var(--backdrop);
  }
  .wrap-panel {
    position: relative;
    width: 1200px;
    height: 667px;
  }
  .wrap-shapes {
    position: absolute;
    inset: 0;
  }
  .contact-phone {
    position: absolute;
    left: 150px;
    top: 258px;
    margin: 0;
    font-family: "Oswald", sans-serif;
    font-weight: 500;
    font-size: 20px;
    line-height: 24px;
    color: var(--ink);
    transform: rotate(-4deg);
    transform-origin: left bottom;
  }
  .contact-email {
    position: absolute;
    left: 292px;
    top: 236px;
    margin: 0;
    font-family: "Roboto Condensed", sans-serif;
    font-weight: 400;
    font-size: 20px;
    line-height: 24px;
    color: var(--cyan);
    transform: rotate(-5deg);
    transform-origin: left bottom;
    white-space: nowrap;
  }
  .service-list {
    position: absolute;
    left: 558px;
    top: 112px;
    margin: 0;
    padding: 0;
    list-style: none;
    font-family: "Oswald", sans-serif;
    font-weight: 500;
    font-size: 20px;
    line-height: 24.5px;
    color: var(--ink);
  }
  .service-list li::before {
    content: "•";
  }
  .brand-name {
    position: absolute;
    left: 282px;
    top: 312px;
    margin: 0;
    font-family: "Antonio", sans-serif;
    font-weight: 300;
    font-size: 76px;
    line-height: 1;
    letter-spacing: 0;
    color: var(--white);
    white-space: nowrap;
  }
</style>
</head>
<body>
  <main class="wrap-panel">
    <svg class="wrap-shapes" width="1200" height="667" viewBox="0 0 1200 667" aria-hidden="true">
      <rect class="base-white" x="60" y="70" width="1080" height="380" rx="40" fill="var(--white)"/>
      <polygon class="accent-stripe" points="130,300 1080,190 1080,212 130,322" fill="var(--cyan)"/>
      <path class="lower-band" d="M130,322 L1080,212 L1080,370 Q1080,440 1010,440 L300,440 Q170,440 150,380 Z" fill="var(--navy)"/>
      <circle class="brand-dot" cx="900" cy="272" r="140" fill="var(--cyan)"/>
    </svg>

    <p class="contact-phone">0412 905 638</p>
    <p class="contact-email">dale@keelstonebuilds.com.au</p>

    <ul class="service-list">
      <li>Commercial Carpentry</li>
      <li>Interior Fitouts</li>
      <li>Plastering</li>
      <li>Suspended Ceilings</li>
      <li>Windows &amp; Doors</li>
    </ul>

    <h1 class="brand-name">KEELSTONE BUILDS</h1>
  </main>
</body>
</html>
```